Brightvale Fluid Systems Corp Business Cards

Business cards to match the logo.

Company is a start up water technology company that has developed a patented system using centrifugal force to separate waste from municipal waste water to produce crystal clear clean water. Product sell starting at 2 million to governments both in the US and international.

Business cards should have a professional look with the target generally engineers.

Target Market(s)

Engineers, Government officials and investors

Industry/Entity Type

Water Treatment

Contact Information for Business Card

Business cards design will be used for 6 to 8 people with job titles. Can use the quote "If there is magic in the planet, it is contained in water." but not required to use quote. Should follow theme of Logo

Font styles to use
Other font styles liked:
• match logo font

Requirements
Nice to have
• Colors to match Logo. Business cards to match style of flow of Logo.
• Emphasis on clean look not a busy look. Clean flowing water.
Should not have
• Pictures of industrial equipment or wastewater

```html
<!DOCTYPE html>
<html lang="en">
<head>
<meta charset="utf-8">
<title>Brightvale Fluid Systems Corp — Business Cards</title>
<link href="https://fonts.googleapis.com/css2?family=Arimo:wght@400;700&family=Playfair+Display:wght@400&display=swap" rel="stylesheet">
<style>
  :root {
    --backdrop: #d5d5d8;
    --paper: #ffffff;
    --navy: #35537a;
    --brand-navy: #2e4d78;
    --accent-blue: #4a90d9;
    --ink-grey: #555a60;
    --shadow: rgba(40, 45, 60, 0.28);
  }
  * { margin: 0; padding: 0; box-sizing: border-box; }
  html, body {
    width: 1200px;
    height: 990px;
    overflow: hidden;
    background: var(--backdrop);
  }
  .sheet {
    width: 1200px;
    height: 990px;
    display: flex;
    align-items: center;
    justify-content: center;
    gap: 60px;
  }
  .card {
    width: 540px;
    height: 300px;
    border-radius: 16px;
    position: relative;
    box-shadow: 0 6px 14px var(--shadow);
  }
  .card--front { background: var(--paper); }
  .card--back {
    background: var(--navy);
    display: flex;
    align-items: center;
    justify-content: center;
  }
  .person {
    position: absolute;
    left: 52px;
    top: 62px;
    font-family: "Arimo", Arial, sans-serif;
  }
  .person__name {
    color: var(--accent-blue);
    font-weight: 700;
    font-size: 15px;
    letter-spacing: 0.2px;
  }
  .person__title {
    color: var(--ink-grey);
    font-size: 13px;
    line-height: 17px;
    margin-top: 3px;
  }
  .wordmark {
    font-family: "Playfair Display", Georgia, serif;
    font-weight: 400;
    text-transform: uppercase;
    line-height: 1.15;
    text-align: center;
  }
  .card--front .wordmark {
    position: absolute;
    right: 52px;
    top: 52px;
    color: var(--brand-navy);
    font-size: 22px;
    letter-spacing: 0.5px;
  }
  .card--back .wordmark {
    color: var(--paper);
    font-size: 34px;
    letter-spacing: 0.8px;
  }
  .contact {
    position: absolute;
    left: 52px;
    bottom: 42px;
    list-style: none;
    font-family: "Arimo", Arial, sans-serif;
    font-size: 13px;
    color: var(--ink-grey);
  }
  .contact li {
    display: flex;
    align-items: center;
    gap: 7px;
    line-height: 17px;
  }
  .contact svg { width: 11px; height: 11px; flex: none; }
  .address {
    position: absolute;
    right: 52px;
    bottom: 42px;
    text-align: right;
    font-family: "Arimo", Arial, sans-serif;
    font-size: 13px;
    line-height: 17px;
    color: var(--ink-grey);
  }
</style>
</head>
<body>
<main class="sheet">
  <section class="card card--front" aria-label="Business card front">
    <div class="person">
      <p class="person__name">MARCUS HALLBECK</p>
      <p class="person__title">Member of Board of<br>Directors</p>
    </div>
    <p class="wordmark">Brightvale Fluid<br>Systems Corp</p>
    <ul class="contact">
      <li>
        <svg viewBox="0 0 12 12" aria-hidden="true"><path fill="#4a90d9" d="M3 1 L4.6 1 L5.2 3.6 L4 4.4 C4.6 5.8 5.9 7.2 7.4 7.9 L8.2 6.8 L11 7.4 L11 9 C11 10.2 10.1 11 9 11 C4.6 10.6 1.4 7.4 1 3 C1 1.9 1.8 1 3 1Z"/></svg>
        555-014-2290
      </li>
      <li>
        <svg viewBox="0 0 12 12" aria-hidden="true"><rect x="0.5" y="2.5" width="11" height="7" fill="#4a90d9"/><path d="M0.8 2.8 L6 6.6 L11.2 2.8" fill="none" stroke="#fff" stroke-width="1"/></svg>
        info@brightvalefs.com
      </li>
      <li>
        <svg viewBox="0 0 12 12" aria-hidden="true"><g fill="none" stroke="#4a90d9" stroke-width="1"><circle cx="6" cy="6" r="5"/><ellipse cx="6" cy="6" rx="2.2" ry="5"/><path d="M1 6 H11 M2 3.5 H10 M2 8.5 H10"/></g></svg>
        www.brightvalefs.com
      </li>
    </ul>
    <p class="address">2480 Harbor Crest Blvd., Suite 210<br>Lakemont, FL 33190</p>
  </section>

  <section class="card card--back" aria-label="Business card back">
    <p class="wordmark">Brightvale Fluid<br>Systems Corp</p>
  </section>
</main>
</body>
</html>
```